Business Card for a Mortgage Agent (myself)

I need a business card for my new job as Mortgage Agent. The Broker's logo is to be on the card as well as the brokerage License number. Not sure if to include a photo or not. Info to be on card.
Dante Roux
Mortgage Agent
Lic # M47105386
Cell: 905-614-2753
Email: danterouxk.ma@fennmail.com
Web: www.karlvostermortgages.com
TPW Brokerage Lic. # 73918

```html
<!DOCTYPE html>
<html lang="en">
<head>
<meta charset="utf-8">
<title>Dante Roux – Mortgage Agent Business Card</title>
<link href="https://fonts.googleapis.com/css2?family=Jost:wght@400;500;600&display=swap" rel="stylesheet">
<style>
  :root {
    --navy: #0a4585;
    --gold: #f7c300;
    --paper: #fbfbfb;
    --backdrop: #e4e4e4;
    --white: #ffffff;
  }
  html, body {
    margin: 0;
    padding: 0;
    width: 1200px;
    height: 930px;
    overflow: hidden;
    background: var(--backdrop);
    font-family: "Jost", "Futura", sans-serif;
  }
  .sheet {
    position: relative;
    width: 1200px;
    height: 930px;
  }
  .card {
    position: absolute;
    left: 250px;
    width: 700px;
    height: 400px;
    box-sizing: border-box;
    box-shadow: 0 6px 18px rgba(0,0,0,0.12);
  }
  .card--front { top: 50px; background: var(--paper); }
  .card--back  { top: 490px; background: var(--navy); }

  .agent-name {
    position: absolute;
    left: 48px;
    top: 50px;
    margin: 0;
    color: var(--gold);
    font-size: 30px;
    font-weight: 500;
    letter-spacing: 0.5px;
    text-transform: uppercase;
    line-height: 1;
  }
  .agent-title {
    position: absolute;
    left: 48px;
    top: 86px;
    margin: 0;
    color: var(--navy);
    font-size: 21px;
    font-weight: 400;
  }
  .rule {
    position: absolute;
    left: 40px;
    right: 40px;
    top: 128px;
    height: 0;
    border-top: 1.5px solid var(--navy);
  }
  .contact-list {
    position: absolute;
    left: 34px;
    top: 146px;
    margin: 0;
    padding: 0;
    list-style: none;
    color: var(--navy);
    font-size: 20px;
    line-height: 30px;
  }
  .contact-list li {
    display: flex;
    align-items: center;
    gap: 10px;
  }
  .contact-list svg { width: 18px; height: 18px; flex: none; }
  .web-domain { color: var(--gold); }

  .brand-mark {
    position: absolute;
    right: 56px;
    top: 34px;
    display: flex;
    align-items: center;
    gap: 12px;
  }
  .brand-mark__square {
    width: 34px;
    height: 34px;
    background: var(--gold);
  }
  .brand-mark__name {
    color: var(--navy);
    font-size: 44px;
    font-weight: 600;
    letter-spacing: 10px;
    line-height: 1;
  }

  .licences {
    position: absolute;
    right: 40px;
    bottom: 40px;
    text-align: right;
    font-size: 21px;
    line-height: 30px;
  }
  .licences p { margin: 0; }
  .licences .label { color: var(--gold); }
  .licences .value { color: var(--navy); }

  .card--back .brand-mark {
    right: auto;
    top: 50%;
    left: 50%;
    transform: translate(-50%, -50%);
    gap: 18px;
  }
  .card--back .brand-mark__square { width: 48px; height: 48px; }
  .card--back .brand-mark__name {
    color: var(--white);
    font-size: 64px;
    letter-spacing: 16px;
  }
</style>
</head>
<body>
<main class="sheet">
  <section class="card card--front" aria-label="Business card front">
    <h1 class="agent-name">Dante Roux</h1>
    <p class="agent-title">Mortgage Agent</p>

    <div class="brand-mark">
      <span class="brand-mark__square"></span>
      <span class="brand-mark__name">TPW</span>
    </div>

    <div class="rule"></div>

    <ul class="contact-list">
      <li>
        <svg viewBox="0 0 24 24" aria-hidden="true"><path fill="#f7c300" d="M6.6 10.8a15.1 15.1 0 0 0 6.6 6.6l2.2-2.2a1 1 0 0 1 1-.25 11.4 11.4 0 0 0 3.6.57 1 1 0 0 1 1 1V20a1 1 0 0 1-1 1A17 17 0 0 1 3 4a1 1 0 0 1 1-1h3.5a1 1 0 0 1 1 1c0 1.25.2 2.45.57 3.57a1 1 0 0 1-.25 1z"/></svg>
        <span>905-614-2753</span>
      </li>
      <li>
        <svg viewBox="0 0 24 24" aria-hidden="true"><rect x="2" y="5" width="20" height="14" fill="#f7c300"/><path d="M2 5l10 8 10-8" fill="none" stroke="#fbfbfb" stroke-width="1.6"/></svg>
        <span>danterouxk.ma@fennmail.com</span>
      </li>
      <li>
        <svg viewBox="0 0 24 24" aria-hidden="true"><circle cx="12" cy="12" r="10" fill="#f7c300"/><path d="M2 12h20M12 2c3 3 3 17 0 20M12 2c-3 3-3 17 0 20" fill="none" stroke="#fbfbfb" stroke-width="1.3"/></svg>
        <span>www.<span class="web-domain">karlvostermortgages</span>.com</span>
      </li>
    </ul>

    <div class="licences">
      <p><span class="label">Lic</span> <span class="value"># M47105386</span></p>
      <p><span class="label">TPW Brokerage Lic.</span> <span class="value"># 73918</span></p>
    </div>
  </section>

  <section class="card card--back" aria-label="Business card back">
    <div class="brand-mark">
      <span class="brand-mark__square"></span>
      <span class="brand-mark__name">TPW</span>
    </div>
  </section>
</main>
</body>
</html>
```